11 x 17 Orvanthes Quote

Design the following quote in a poster.

"First say to yourself what you would be; then do what you have to do." - Orvanthes

See here for inspiration - https://prints.mornbrekal.com/

Quote

```html
<!DOCTYPE html>
<html lang="en">
<head>
<meta charset="utf-8">
<title>Orvanthes Quote Poster</title>
<link rel="stylesheet" href="https://fonts.googleapis.com/css2?family=Permanent+Marker&display=block">
<style>
  :root {
    --backdrop: #e4e4e4;
    --paper: #fdfdfd;
    --ink: #111111;
    --accent: #c61d2a;
    --brush: "Permanent Marker", Impact, "Arial Black", sans-serif;
  }
  html, body {
    margin: 0;
    padding: 0;
    width: 923px;
    height: 1200px;
    overflow: hidden;
    background: var(--backdrop);
  }
  .poster {
    position: absolute;
    left: 130px;
    top: 182px;
    width: 660px;
    height: 923px;
    background: var(--paper);
  }
  .quote {
    margin: 0;
    font-family: var(--brush);
    color: var(--ink);
    text-transform: uppercase;
    line-height: 1;
  }
  .quote-line {
    position: absolute;
    left: 0;
    right: 0;
    display: flex;
    justify-content: center;
    align-items: center;
    gap: 8px;
    white-space: nowrap;
  }
  .stack {
    display: flex;
    flex-direction: column;
    align-items: center;
    line-height: 0.9;
  }
  .pair {
    display: flex;
    flex-direction: column;
    align-items: flex-start;
    line-height: 0.95;
  }
  .accent { color: var(--accent); }
  .mark { align-self: flex-start; }

  /* line 1 */
  .line-first { top: 232px; }
  .line-first .mark { font-size: 64px; margin-right: -6px; }
  .word-first { font-size: 96px; letter-spacing: -1px; }
  .stack-say { font-size: 17px; }
  .stack-to { font-size: 38px; line-height: 0.82; }

  /* line 2 */
  .line-yourself { top: 346px; gap: 10px; }
  .word-yourself { font-size: 66px; letter-spacing: -1px; }
  .pair-would { font-size: 24px; }
  .pair-would .spaced { letter-spacing: 6px; }

  /* line 3 */
  .line-be { top: 430px; gap: 10px; }
  .word-be { font-size: 110px; letter-spacing: -2px; }
  .stack-then { font-size: 17px; }
  .pair-you { align-items: center; }
  .word-dowhat { font-size: 28px; }
  .word-you { font-size: 72px; line-height: 0.9; }

  /* line 4 */
  .line-do { top: 556px; gap: 12px; }
  .stack-have { font-size: 22px; }
  .stack-to-red { font-size: 54px; line-height: 0.82; }
  .word-do { font-size: 124px; letter-spacing: -3px; }
  .word-do .stop { color: var(--ink); }
  .line-do .mark { font-size: 64px; margin-left: -4px; }

  .author {
    position: absolute;
    left: 0;
    right: 0;
    top: 724px;
    margin: 0;
    text-align: center;
    font-family: var(--brush);
    font-size: 30px;
    letter-spacing: 1px;
    text-transform: uppercase;
    color: var(--ink);
  }
</style>
</head>
<body>
  <main class="poster">
    <blockquote class="quote" aria-label="First say to yourself what you would be; then do what you have to do.">
      <div class="quote-line line-first">
        <span class="mark">"</span>
        <span class="word-first">First</span>
        <span class="stack stack-say"><span>S</span><span>A</span><span>Y</span></span>
        <span class="stack stack-to"><span>T</span><span>O</span></span>
      </div>
      <div class="quote-line line-yourself">
        <span class="word-yourself">Yourself</span>
        <span class="pair pair-would"><span>What you</span><span class="spaced">Would</span></span>
      </div>
      <div class="quote-line line-be">
        <span class="word-be">Be;</span>
        <span class="stack stack-then"><span>T</span><span>H</span><span>E</span><span>N</span></span>
        <span class="pair pair-you"><span class="word-dowhat">Do what</span><span class="word-you">You</span></span>
      </div>
      <div class="quote-line line-do">
        <span class="stack stack-have"><span>H</span><span>A</span><span>V</span><span>E</span></span>
        <span class="stack stack-to-red accent"><span>T</span><span>O</span></span>
        <span class="word-do accent">Do<span class="stop">.</span></span>
        <span class="mark">"</span>
      </div>
    </blockquote>
    <p class="author">Orvanthes</p>
  </main>
</body>
</html>
```